Elegant wordpress web page for wedding rental of hand sanitizers

We want to rent our hand sanitizing towers out for high-end weddings. We need a very elegant, sophisticated page that describes our offering. You can see an ugly first draft here: purvant.com/weddings
Target Market(s)
Wedding planners, wedding parents
Number of Pages Required
1 page
Font styles to use
Serif
Script
Colors
Designer to choose colors to be used in the design.
Requirements
Nice to have
- Two wedding-related sites for inspiration: lacetrellisweddings-dot-com and fennoreventservices-dot-com

```html
<!DOCTYPE html>
<html lang="en">
<head>
<meta charset="utf-8">
<title>Purvant — Wedding Sanitizer Stations</title>
<link href="https://fonts.googleapis.com/css2?family=Cormorant+Garamond:ital,wght@0,500;1,400;1,500&family=Roboto:wght@400;500;700&display=swap" rel="stylesheet">
<style>
:root{
  --white:#ffffff;
  --ink:#2b2b2b;
  --body:#444444;
  --muted:#6b6b6b;
  --beige:#ebe7d3;
  --beige-deep:#dcd6bb;
  --grey:#b5b5b5;
  --button:#bdbdbd;
  --accent:#3a8fd8;
  --footer:#121820;
  --footer-line:#2e3640;
  --panel:rgba(60,60,60,.55);
}
*{box-sizing:border-box;margin:0;padding:0}
html,body{width:1200px;height:5000px;overflow:hidden}
body{position:relative;background:var(--white);font-family:'Roboto',Arial,sans-serif;color:var(--body)}
.abs{position:absolute}
.script{font-family:'Cormorant Garamond',Georgia,serif;font-style:italic;font-weight:500;color:var(--ink)}
.btn{position:absolute;background:var(--button);color:var(--ink);font:700 13px 'Roboto',Arial,sans-serif;letter-spacing:.3px;display:flex;align-items:center;justify-content:center;height:39px;padding:0 16px;text-transform:uppercase}
.btn-outline{position:absolute;border:1.5px solid var(--ink);color:var(--ink);font:500 12px 'Roboto',Arial,sans-serif;height:32px;display:flex;align-items:center;justify-content:center;padding:0 12px}
.accent-rule{position:absolute;height:2px;width:52px;background:var(--accent)}
.photo{position:absolute}

/* hero */
.hero{position:absolute;left:0;top:0;width:1200px;height:760px;overflow:hidden}
.hero-photo{position:absolute;inset:0;background:linear-gradient(100deg,#4c5a3f 0%,#8a7a5e 30%,#b9a88c 55%,#6d6a55 80%,#3d4632 100%)}
.hero-stand{position:absolute;left:180px;top:80px;width:240px;height:570px;border-radius:26px 26px 0 0;background:linear-gradient(180deg,#e8dcd2 0%,#b98a86 45%,#efefef 70%,#d8d8d8 100%)}
.brand{position:absolute;left:98px;top:38px;display:flex;align-items:center;gap:10px;color:var(--white);font:700 44px 'Roboto',Arial,sans-serif}
.brand-dot{width:14px;height:14px;border-radius:50%;background:var(--white)}
.nav{position:absolute;top:72px;left:459px;display:flex;gap:46px;color:var(--white);font:500 15px 'Roboto',Arial,sans-serif}
.topbar{position:absolute;top:15px;left:773px;display:flex;align-items:center;gap:20px}
.phone{display:flex;align-items:center;gap:8px;color:var(--white);font:500 16px 'Roboto',Arial,sans-serif}
.phone-ico{width:30px;height:30px;border-radius:50%;background:var(--accent);display:flex;align-items:center;justify-content:center}
.book{background:var(--white);color:var(--ink);font:700 13px 'Roboto',Arial,sans-serif;padding:0 18px;height:34px;display:flex;align-items:center}
.hero-panel{position:absolute;left:615px;top:180px;width:503px;height:317px;background:var(--panel);padding:20px 20px}
.hero-panel h1{font-family:'Cormorant Garamond',Georgia,serif;font-style:italic;font-weight:400;color:var(--white);font-size:56px;line-height:47px}
.hero-panel h2{font-family:'Cormorant Garamond',Georgia,serif;font-style:italic;font-weight:400;color:var(--white);font-size:42px;margin-top:8px}
.arrow{position:absolute;top:358px}
.dots{position:absolute;top:702px;left:563px;display:flex;gap:8px}
.dots span{width:12px;height:12px;border-radius:50%;border:1.5px solid var(--white)}
.dots span.on{background:var(--white)}

/* features */
.features-title{left:118px;top:842px;font-size:44px;line-height:42px}
.feature-list{position:absolute;left:116px;top:944px;width:470px;list-style:none}
.feature-list li{margin-bottom:20px}
.feature-list h3{display:flex;align-items:center;gap:6px;font:500 17px 'Roboto',Arial,sans-serif;color:var(--ink)}
.feature-list p{font-size:16px;line-height:23px;color:var(--body);padding-left:20px}
.bullet{width:14px;height:14px;border-radius:50%;border:2px solid var(--ink);display:inline-flex;align-items:center;justify-content:center}
.bullet::after{content:"";width:6px;height:6px;border-radius:50%;background:var(--ink)}

/* customize */
.customize-title{left:0;width:1200px;top:1526px;text-align:center;font-size:44px;line-height:44px}
.step{position:absolute;width:230px}
.step h4{font:700 14px 'Roboto',Arial,sans-serif;color:var(--ink);margin-bottom:3px}
.step p{font-size:14px;line-height:20px;color:var(--body);margin-bottom:10px}
.step.left{text-align:right}
.step.left .btn-outline{position:relative;display:inline-flex}
.step.right .btn-outline{position:relative;display:inline-flex}
.mini{position:absolute;width:104px;height:104px;border-radius:50%;border:3px solid var(--white);box-shadow:0 0 0 1.5px var(--ink)}

/* about */
.about-title{left:631px;top:2484px;font-size:46px}
.about-text{position:absolute;left:631px;top:2546px;width:490px;font-size:17px;line-height:26.8px;color:var(--body)}

/* testimonial */
.greet-title{left:0;width:1200px;top:3082px;text-align:center;font-size:44px;line-height:44px}
.greet-sub{position:absolute;left:0;width:1200px;top:3208px;text-align:center;font:500 16px 'Roboto',Arial,sans-serif;color:var(--ink)}
.quote{position:absolute;left:449px;top:3273px;width:575px;font-style:italic;font-size:17px;line-height:30px;color:var(--body)}
.quote-name{position:absolute;left:449px;top:3432px;font:500 19px 'Roboto',Arial,sans-serif;color:var(--ink)}
.stars{position:absolute;left:449px;top:3464px;display:flex;gap:2px}

/* gallery */
.gallery-title{left:0;width:1200px;top:3676px;text-align:center;font-size:46px}
.gallery-sub{position:absolute;left:230px;width:740px;top:3752px;text-align:center;font:500 15px 'Roboto',Arial,sans-serif;line-height:22px;color:var(--ink)}

/* footer */
.footer-head{position:absolute;font:700 19px 'Roboto',Arial,sans-serif;color:var(--white)}
.field{position:absolute;border:1px solid #7a828c;color:#c9ced4;font-size:12px;padding:6px 7px}
.submit{position:absolute;left:99px;top:4851px;width:130px;height:34px;background:var(--white);color:var(--ink);font:700 13px 'Roboto',Arial,sans-serif;display:flex;align-items:center;justify-content:center}
.contact-row{position:absolute;left:629px;display:flex;gap:10px;color:var(--white);font-size:13px;line-height:18px}
.contact-ico{width:34px;height:34px;border-radius:50%;border:1.5px solid var(--white);display:flex;align-items:center;justify-content:center;flex:none}
.quick{position:absolute;left:969px;top:4690px;list-style:none;color:var(--white);font-size:13px;line-height:29px}
.copyright{position:absolute;left:99px;top:4956px;font-size:13px;color:var(--white)}
.social{position:absolute;top:4946px;left:952px;display:flex;gap:8px}
.social span{width:33px;height:33px;border-radius:50%;border:1.5px solid var(--white)}
</style>
</head>
<body>

<!-- HERO -->
<section class="hero">
  <div class="hero-photo" role="img" aria-label="Outdoor wedding ceremony aisle with chairs and flower arrangements, softly blurred"></div>
  <div class="hero-stand" role="img" aria-label="Hand sanitizer tower with a couple's wedding photo banner and a floral spout"></div>
  <div class="brand"><span>purvant</span><span class="brand-dot"></span></div>
  <div class="topbar">
    <div class="phone"><span class="phone-ico"><svg width="16" height="16" viewBox="0 0 24 24"><path fill="#fff" d="M6.6 10.8c1.4 2.8 3.8 5.1 6.6 6.6l2.2-2.2c.3-.3.7-.4 1-.2 1.1.4 2.3.6 3.6.6.6 0 1 .4 1 1V20c0 .6-.4 1-1 1C10.6 21 3 13.4 3 4c0-.6.4-1 1-1h3.5c.6 0 1 .4 1 1 0 1.3.2 2.5.6 3.6.1.3 0 .7-.2 1z"/></svg></span>+1 215-555-0148</div>
    <div class="book">BOOK ONLINE</div>
  </div>
  <nav class="nav"><span>HOME</span><span>ABOUT</span><span>PRODUCTS</span><span>INDUSTRY SOLUTIONS</span><span>CONTACT</span></nav>
  <div class="hero-panel">
    <h1>Welcome your friends<br>with something truly<br>unique:</h1>
    <h2>A customized hand sanitizer</h2>
  </div>
  <div class="btn" style="left:633px;top:437px;height:40px">CHECK PRICE &amp;AVAILABILITY</div>
  <svg class="arrow" style="left:58px" width="24" height="36" viewBox="0 0 24 36"><path d="M18 2 4 18l14 16" fill="none" stroke="#fff" stroke-width="2"/></svg>
  <svg class="arrow" style="left:1136px" width="24" height="36" viewBox="0 0 24 36"><path d="M6 2l14 16L6 34" fill="none" stroke="#fff" stroke-width="2"/></svg>
  <svg class="abs" style="left:0;top:560px" width="1200" height="200" viewBox="0 0 1200 200">
    <path d="M0 30 Q600 190 1200 30 L1200 200 L0 200Z" fill="var(--grey)"/>
    <path d="M0 62 Q600 198 1200 62 L1200 200 L0 200Z" fill="var(--white)"/>
  </svg>
  <div class="dots"><span class="on"></span><span></span><span></span><span></span></div>
</section>

<!-- FEATURES -->
<h2 class="abs script features-title">What Makes Our Sanitizing<br>Station Better?</h2>
<ul class="feature-list">
  <li><h3><span class="bullet"></span>Durable and Reliable</h3><p>4 ft tall, weighing almost 40 pounds</p></li>
  <li><h3><span class="bullet"></span>Touchless and Automatic</h3><p>the preferred way to sanitize</p></li>
  <li><h3><span class="bullet"></span>Battery Powered and Wireless</h3><p>locate it anywhereFilled with your choice from our wide range of sanitizing solutions</p></li>
  <li><h3><span class="bullet"></span>Easily Customizable</h3><p>choose your preferred backdrop and spout</p></li>
</ul>
<div class="btn" style="left:116px;top:1227px">CHECK PRICE &amp;AVAILABILITY</div>
<div class="photo" style="left:628px;top:828px;width:470px;height:480px;border-radius:50%;background:radial-gradient(circle at 45% 40%,#c9a99c,#7b7160 55%,#4d4b3e)" role="img" aria-label="Sanitizer tower with a wedding couple banner and flowers, in a round frame"></div>

<!-- CUSTOMIZE -->
<svg class="abs" style="left:0;top:1398px" width="1200" height="980" viewBox="0 0 1200 980">
  <path d="M0 70 Q600 -68 1200 70 L1200 900 Q600 1040 0 900Z" fill="var(--grey)"/>
  <path d="M0 102 Q600 -40 1200 102 L1200 872 Q600 1012 0 872Z" fill="var(--beige)"/>
</svg>
<h2 class="abs script customize-title">Customize Your Sanitizer<br>With Any Photo, Any Size, Any Shape</h2>
<div class="accent-rule" style="left:574px;top:1630px"></div>
<svg class="abs" style="left:390px;top:1716px" width="420" height="420" viewBox="0 0 420 420"><circle cx="210" cy="210" r="204" fill="none" stroke="var(--ink)" stroke-width="2.5"/></svg>
<div class="photo" style="left:530px;top:1664px;width:124px;height:490px;background:linear-gradient(180deg,#d8c7bd 0%,#b58d88 38%,#f2f2f2 45%,#e3e3e3 100%)" role="img" aria-label="Full sanitizer tower with couple photo banner on a white stand"></div>
<div class="mini" style="left:346px;top:1786px;background:linear-gradient(135deg,#6c5a4b,#cbb7a5)" role="img" aria-label="Couple photo"></div>
<div class="mini" style="left:740px;top:1786px;background:linear-gradient(135deg,#a7a8a6,#e3e0db)" role="img" aria-label="Banner sizes and shapes"></div>
<div class="mini" style="left:352px;top:1986px;background:linear-gradient(135deg,#2f4a2c,#a6a47e)" role="img" aria-label="Decorated spout with flowers"></div>
<div class="mini" style="left:740px;top:1986px;background:linear-gradient(135deg,#8e8a84,#e1d6d2)" role="img" aria-label="Team installing a sanitizer"></div>
<div class="step left" style="left:100px;top:1790px"><h4>CHOOSE A PHOTO</h4><p>The happy couple, the proud parents, even the family dog</p><span class="btn-outline">CUSTOMIZATION</span></div>
<div class="step right" style="left:858px;top:1790px"><h4>PICK A SIZE AND SHAPE</h4><p>Any size banner up to 24 x 36 in. Any shape. Send us the photo and we'll print and install it.</p><span class="btn-outline">CUSTOMIZATION</span></div>
<div class="step left" style="left:106px;top:1984px"><h4>DECORATE THE SPOUT</h4><p>Use one of our standard decorations - a wedding cake or a flower vase</p><span class="btn-outline">CUSTOMIZATION</span></div>
<div class="step right" style="left:858px;top:1984px"><h4>TEAM</h4><p>Our team decorates and delivers the sanitizer</p><span class="btn-outline">CUSTOMIZATION</span></div>
<div class="btn" style="left:482px;top:2212px">CHECK PRICE &amp;AVAILABILITY</div>

<!-- ABOUT -->
<div class="photo" style="left:107px;top:2459px;width:470px;height:470px;border-radius:50%;background:radial-gradient(circle at 50% 45%,#f1eef3,#d7cfd6 55%,#9d8c7a)" role="img" aria-label="White room with flower arrangements on pedestals beside a sanitizer station"></div>
<h2 class="abs script about-title">About Us</h2>
<p class="about-text">Sed ut perspiciatis unde omnis iste natuerror sit voluptatem accusantium doloremque laudantium, totam reperiam, eaque ipsa quae ab illo inventore veritatis et quasi achitecto beatae vitae dicta sunt explicabo. Nemo enim ipsa voluptatem quia voluptas sit aspernatur aut odit augit, sed quia consequuntur magni dolores eos qui ratione votatem sequi nesciunt. Neque porro quisquam esem ipsum quia dolor sit amet, consectetur, adipisci velit, sed quia non numquam eius modi tempora incidunt ut labore et dolore magnam aliquam quaerat voluptatem.</p>
<div class="btn" style="left:631px;top:2839px">CHECK PRICE &amp;AVAILABILITY</div>

<!-- TESTIMONIAL -->
<svg class="abs" style="left:0;top:3016px" width="1200" height="590" viewBox="0 0 1200 590">
  <path d="M0 76 Q600 -72 1200 76 L1200 500 Q600 650 0 500Z" fill="var(--grey)"/>
  <path d="M0 108 Q600 -40 1200 108 L1200 470 Q600 620 0 470Z" fill="var(--beige)"/>
</svg>
<h2 class="abs script greet-title">Greet your friends and family with a<br>personalized act of care</h2>
<div class="accent-rule" style="left:574px;top:3188px"></div>
<p class="greet-sub">Make your friends and family feel welcome and safe.</p>
<svg class="abs" style="left:124px;top:3358px" width="20" height="32" viewBox="0 0 20 32"><path d="M16 2 4 16l12 14" fill="none" stroke="var(--ink)" stroke-width="3"/></svg>
<svg class="abs" style="left:1056px;top:3358px" width="20" height="32" viewBox="0 0 20 32"><path d="M4 2l12 14L4 30" fill="none" stroke="var(--ink)" stroke-width="3"/></svg>
<div class="photo" style="left:178px;top:3270px;width:210px;height:210px;border-radius:50%;border:4px solid var(--white);background:linear-gradient(135deg,#a08a6f,#5a4e3c 60%,#d2c6b2)" role="img" aria-label="Wedding couple walking out under a floral arch"></div>
<svg class="abs" style="left:404px;top:3276px" width="40" height="32" viewBox="0 0 40 32"><path d="M2 30V18C2 8 8 2 16 1v5c-5 1-7 5-7 9h7v15zM22 30V18c0-10 6-16 14-17v5c-5 1-7 5-7 9h7v15z" fill="var(--ink)"/></svg>
<p class="quote">Sed ut perspiciatis unde omnis iste natus error sit volutem accusantium doloremque laudantium, totam rem aperiam, eaque ipsa quae ab illo inventore veritatis et quasi architecto beatae vitae dicta sunt explicabo. Nemo enim ipsam voluptatem quia voluptas sit aspernatur aut odit aut fugit, sed quia consequuntur magni</p>
<svg class="abs" style="left:966px;top:3400px" width="40" height="32" viewBox="0 0 40 32"><path d="M38 2v12c0 10-6 16-14 17v-5c5-1 7-5 7-9h-7V2zM18 2v12c0 10-6 16-14 17v-5c5-1 7-5 7-9H4V2z" fill="var(--ink)"/></svg>
<p class="quote-name">Elena Marsh - Purvant</p>
<div class="stars">
  <svg width="20" height="19" viewBox="0 0 24 23"><path d="M12 0l3.5 7.6 8.5.9-6.3 5.7 1.8 8.3L12 18.3 4.5 22.5l1.8-8.3L0 8.5l8.5-.9z" fill="var(--ink)"/></svg>
  <svg width="20" height="19" viewBox="0 0 24 23"><path d="M12 0l3.5 7.6 8.5.9-6.3 5.7 1.8 8.3L12 18.3 4.5 22.5l1.8-8.3L0 8.5l8.5-.9z" fill="var(--ink)"/></svg>
  <svg width="20" height="19" viewBox="0 0 24 23"><path d="M12 0l3.5 7.6 8.5.9-6.3 5.7 1.8 8.3L12 18.3 4.5 22.5l1.8-8.3L0 8.5l8.5-.9z" fill="var(--ink)"/></svg>
  <svg width="20" height="19" viewBox="0 0 24 23"><path d="M12 0l3.5 7.6 8.5.9-6.3 5.7 1.8 8.3L12 18.3 4.5 22.5l1.8-8.3L0 8.5l8.5-.9z" fill="var(--ink)"/></svg>
  <svg width="20" height="19" viewBox="0 0 24 23"><path d="M12 0l3.5 7.6 8.5.9-6.3 5.7 1.8 8.3L12 18.3 4.5 22.5l1.8-8.3L0 8.5l8.5-.9z" fill="var(--ink)"/></svg>
</div>

<!-- GALLERY -->
<h2 class="abs script gallery-title">Our Photo Gallery</h2>
<div class="accent-rule" style="left:574px;top:3736px"></div>
<p class="gallery-sub">Lorem ipsum dolor sit amet, consectetur adipiscing elit, sed do eiusmod tempor incididunt ut labore et dolore magna aliqua. Quis ipsum suspendisse ultrices gravida.</p>
<div class="photo" style="left:99px;top:3832px;width:324px;height:272px;background:linear-gradient(160deg,#c48a3a,#5f5a3e 55%,#3a3a32)" role="img" aria-label="Autumn outdoor wedding ceremony with guests"></div>
<div class="photo" style="left:439px;top:3832px;width:324px;height:272px;background:linear-gradient(160deg,#7a5a45,#e7e2dc 55%,#c8c0b8)" role="img" aria-label="Sanitizer tower at an indoor reception"></div>
<div class="photo" style="left:777px;top:3832px;width:324px;height:272px;background:linear-gradient(160deg,#5a6b4a,#cbb5a5 50%,#d98a92)" role="img" aria-label="Sanitizer tower beside an outdoor aisle with flowers"></div>
<div class="photo" style="left:99px;top:4119px;width:324px;height:272px;background:linear-gradient(160deg,#3f5a36,#d8c8c2 55%,#f1f1f1)" role="img" aria-label="Sanitizer tower with cake spout by a garden hedge"></div>
<div class="photo" style="left:439px;top:4119px;width:324px;height:272px;background:linear-gradient(160deg,#efeaf0,#c9a0a6 55%,#b08f5a)" role="img" aria-label="Flower arrangements on white pedestals"></div>
<div class="photo" style="left:777px;top:4119px;width:324px;height:272px;background:linear-gradient(160deg,#dcdcdc,#c8b0a8 50%,#f2f2f2)" role="img" aria-label="Sanitizer tower at a bright venue"></div>
<div class="btn" style="left:482px;top:4417px">CHECK PRICE &amp;AVAILABILITY</div>

<!-- FOOTER -->
<svg class="abs" style="left:0;top:4530px" width="1200" height="470" viewBox="0 0 1200 470">
  <path d="M0 12 L1200 0 L1200 470 L0 470Z" fill="var(--grey)"/>
  <path d="M0 42 L1200 12 L1200 470 L0 470Z" fill="var(--footer)"/>
  <line x1="99" y1="403" x2="1101" y2="403" stroke="var(--footer-line)" stroke-width="1"/>
</svg>
<h3 class="footer-head" style="left:99px;top:4646px">BOOK ONLINE</h3>
<div class="field" style="left:99px;top:4694px;width:200px;height:34px">First Name</div>
<div class="field" style="left:305px;top:4694px;width:200px;height:34px">Last Name</div>
<div class="field" style="left:99px;top:4735px;width:200px;height:34px">Phone Number</div>
<div class="field" style="left:305px;top:4735px;width:200px;height:34px">Email Address</div>
<div class="field" style="left:99px;top:4777px;width:406px;height:60px">Message</div>
<div class="submit">SUBMIT</div>

<h3 class="footer-head" style="left:629px;top:4646px">CONTACT US</h3>
<div class="contact-row" style="top:4688px"><span class="contact-ico"><svg width="14" height="18" viewBox="0 0 14 18"><path d="M7 0a7 7 0 0 0-7 7c0 5 7 11 7 11s7-6 7-11a7 7 0 0 0-7-7zm0 9.5A2.5 2.5 0 1 1 7 4.5a2.5 2.5 0 0 1 0 5z" fill="#fff"/></svg></span><span>Purvant<br>48 Larkmoor Lane Anywhere<br>USA 21212</span></div>
<div class="contact-row" style="top:4755px"><span class="contact-ico"><svg width="16" height="16" viewBox="0 0 24 24"><path fill="#fff" d="M6.6 10.8c1.4 2.8 3.8 5.1 6.6 6.6l2.2-2.2c.3-.3.7-.4 1-.2 1.1.4 2.3.6 3.6.6.6 0 1 .4 1 1V20c0 .6-.4 1-1 1C10.6 21 3 13.4 3 4c0-.6.4-1 1-1h3.5c.6 0 1 .4 1 1 0 1.3.2 2.5.6 3.6.1.3 0 .7-.2 1z"/></svg></span><span>Phone:<br>+1 215-555-0148</span></div>
<div class="contact-row" style="top:4810px"><span class="contact-ico"><svg width="16" height="12" viewBox="0 0 16 12"><rect x=".75" y=".75" width="14.5" height="10.5" fill="none" stroke="#fff" stroke-width="1.5"/><path d="M1 1l7 6 7-6" fill="none" stroke="#fff" stroke-width="1.5"/></svg></span><span>E-Mail:<br>mara@purvant.com</span></div>

<h3 class="footer-head" style="left:969px;top:4646px">QUICK LINKS</h3>
<ul class="quick"><li>Home</li><li>About</li><li>Products</li><li>Industry Solutions</li><li>Contact</li></ul>

<p class="copyright">Copyright © 2021 PURVANT, LLC. All rights reserved.</p>
<div class="social"><span></span><span></span><span></span><span></span></div>

</body>
</html>
```